Idea for facelift on local Hong Kong family business website to get ready for International business

We are a family business in Hong Kong doing high quality aluminium and fibre glass ladder systems. We are currently exploring International markets and are looking for ideas for web site design facelift.

Because we want to attract good talents, we are not asking the designer to finish the work. The best idea wins, even if unfinished.

It is however most important that sample HTML / CSS code is done to show that the designer knows responsive web, and that it is feasible, not just looks good.

Depending on the outcome, we will put out additional tasks for further materialising of the design and for full coding of the web site

This is the current web-site for the ladder brand we will be promoting overseas:

https://www.vornel-climb.com

This is the parent company, which does business in Hong Kong (for reference only, subsequent additional facelift tasks will come after we have finished the product site.

http://www.pimsonco.com.hk

Remember, do just enough to show us you really know responsive web design including coding. It is ok use templates. We are looking for good idea from good designer who also knows HTML and CSS. For this project we are looking for quality, not quantity.

Target Market(s)

International customers

Industry/Entity Type

Hardware / Ladder Systems

Coding

Coded - Design and coding required

Number of Pages Required

3 page

Requirements
Must have
• Enough HTML CSS and optionally JS to show designer knows responsive web design coding

```html
<!DOCTYPE html>
<html lang="en">
<head>
<meta charset="utf-8">
<meta name="viewport" content="width=767">
<title>VORNEL – Ladders Specialist</title>
<link href="https://fonts.googleapis.com/css2?family=Poppins:wght@500;600;700&family=Roboto:wght@400;500&display=swap" rel="stylesheet">
<style>
:root{
  --red:#d3202e;
  --ink:#1d1d1f;
  --text:#333;
  --green:#8cc63f;
  --orange:#f05a28;
  --sky:#6fcff5;
  --panel:rgba(255,255,255,.93);
}
*{box-sizing:border-box;margin:0;padding:0}
html,body{width:767px;height:1200px;overflow:hidden;background:#fff}
body{font-family:'Roboto',sans-serif;color:var(--text)}
.page{position:relative;width:767px;height:1200px;overflow:hidden}

/* header */
.site-header{position:absolute;top:0;left:0;width:767px;height:81px;background:#f7f7f8;z-index:3}
.nav{position:absolute;top:36px;display:flex;gap:11px;font-size:7.2px;color:var(--ink);letter-spacing:.1px}
.nav-left{left:27px}
.nav-right{right:27px}
.brand-badge{position:absolute;left:334px;top:8px;width:100px;height:100px;border-radius:50%;background:#fff;border:2px solid #ddd;display:flex;align-items:center;justify-content:center;z-index:4;box-shadow:0 1px 4px rgba(0,0,0,.12)}
.brand-name{font-family:'Poppins',sans-serif;font-weight:700;font-size:14px;color:var(--red);letter-spacing:.5px}

/* hero */
.hero{position:absolute;top:81px;left:0;width:767px;height:280px;background:linear-gradient(100deg,#b9a99c 0%,#c9bfb6 30%,#9aa55a 55%,#7fa42c 75%,#5d6b3c 100%)}
.hero-shade{position:absolute;inset:0;background:rgba(20,20,20,.25)}
.hero-copy{position:absolute;top:106px;left:0;width:767px;text-align:center;color:#fff}
.hero-title{font-family:'Poppins',sans-serif;font-weight:700;font-size:31px;line-height:1.1}
.hero-sub{font-family:'Poppins',sans-serif;font-weight:500;font-size:11px;color:var(--green);margin-top:13px}
.hero-text{font-size:8.5px;line-height:15px;margin-top:10px}
.btn-solid{display:inline-block;margin-top:10px;width:107px;height:27px;line-height:27px;background:var(--red);color:#fff;font-family:'Poppins',sans-serif;font-weight:500;font-size:8.5px;border-radius:2px}

.lines{position:absolute;top:0;left:0;z-index:2}
.line-tag{position:absolute;font-family:'Poppins',sans-serif;font-weight:600;font-size:14px;color:var(--ink);z-index:2;display:flex;align-items:center;gap:6px;white-space:nowrap}
.line-tag .dot{width:12px;height:12px;border-radius:50%;flex:none}
.tag-up{left:152px;top:371px}
.tag-down{left:330px;top:404px}
.tag-home{left:550px;top:371px}

/* products */
.section-title{position:absolute;top:520px;left:0;width:767px;text-align:center;font-family:'Poppins',sans-serif;font-weight:600;font-size:20px;color:var(--ink)}
.card{position:absolute;overflow:hidden}
.panel{position:absolute;background:var(--panel);display:flex;flex-direction:column;align-items:center;text-align:left}
.panel-wide{left:21px;right:24px;top:18px;bottom:18px;padding:8px 19px 0}
.panel-narrow{left:14px;right:14px;top:15px;bottom:14px;padding:8px 7px 0}
.card-brand{font-family:'Poppins',sans-serif;font-weight:700;font-size:8px;color:var(--orange);height:38px;display:flex;align-items:flex-end;padding-bottom:2px}
.card-text{font-size:7px;line-height:12.6px;color:var(--text);margin-top:8px;align-self:stretch}
.btn-outline{display:block;width:76px;height:24px;line-height:22px;border:1.2px solid var(--red);color:var(--red);text-align:center;font-size:7.2px;border-radius:2px;margin-top:8px}

.c-ladder{left:27px;top:568px;width:354px;height:184px;background:linear-gradient(120deg,#d9d8dc,#e7e4ea 60%,#dccfe0)}
.c-logistic{left:386px;top:568px;width:175px;height:178px;background:linear-gradient(180deg,#e5e5e7,#cfcfd2)}
.c-castor{left:566px;top:568px;width:174px;height:178px;background:linear-gradient(180deg,#e6e6e8,#d4d4d6)}
.c-tools{left:27px;top:758px;width:175px;height:178px;background:linear-gradient(180deg,#e4e4e6,#cacacd)}
.c-custom{left:207px;top:758px;width:174px;height:178px;background:linear-gradient(90deg,#f2f2f3,#bdbdc0)}
.c-scaffold{left:386px;top:752px;width:354px;height:184px;background:linear-gradient(120deg,#d6d6d8,#ebebec 50%,#d8d8da)}
.c-scaffold .card-text{margin-top:12px}

/* footer */
.site-footer{position:absolute;left:0;top:1050px;width:767px;height:150px}
.footer-bg{position:absolute;top:0;left:0}
.footer-badge{top:-8px}
.contact{position:absolute;left:27px;top:56px;font-size:7.2px;color:var(--ink);font-weight:500}
.contact li{list-style:none;display:flex;align-items:flex-start;gap:7px;margin-bottom:9px;line-height:11px}
.contact svg{flex:none;margin-top:1px}
.social{position:absolute;right:35px;top:94px;display:flex;gap:12px}
.social span{display:block;width:17px;height:17px;border-radius:50%;background:var(--red)}
.copyright{position:absolute;bottom:4px;left:0;width:767px;text-align:center;font-size:7px;color:var(--ink)}
</style>
</head>
<body>
<div class="page">

  <header class="site-header">
    <nav class="nav nav-left"><span>VORNEL</span><span>CUSTOM MADE SAFETY EQUIPMENTS</span><span>TO BE DISTRIBUTOR</span></nav>
    <nav class="nav nav-right"><span>SAFETY INFO</span><span>ABOUT</span></nav>
  </header>
  <div class="brand-badge"><span class="brand-name">VORNEL</span></div>

  <section class="hero" role="img" aria-label="Photo of a smiling worker in a red helmet and hi-vis jacket with climbing harness">
    <div class="hero-shade"></div>
    <div class="hero-copy">
      <h1 class="hero-title">Ladders Specialist</h1>
      <p class="hero-sub">Work at Height Safety Tools Equipment</p>
      <p class="hero-text">Our mission is to make sure you work safely no matter at work or at<br>home to prevent any injury especially in the construction industry.</p>
      <a class="btn-solid">SHOP NOW</a>
    </div>
  </section>

  <svg class="lines" width="767" height="480" viewBox="0 0 767 480" aria-hidden="true">
    <defs><linearGradient id="steel" x1="0" y1="0" x2="0" y2="1"><stop offset="0" stop-color="#ececee"/><stop offset="1" stop-color="#d8d8da"/></linearGradient></defs>
    <path d="M0,323 Q384,395 767,323 L767,476 L0,476 Z" fill="url(#steel)"/>
  </svg>
  <div class="line-tag tag-up"><i class="dot" style="background:var(--orange)"></i><span>Rise Line</span></div>
  <div class="line-tag tag-down"><i class="dot" style="background:var(--green)"></i><span>Descent Line</span></div>
  <div class="line-tag tag-home"><i class="dot" style="background:var(--sky)"></i><span>Home Line</span></div>

  <h2 class="section-title">VORNEL Products include</h2>

  <article class="card c-ladder" role="img" aria-label="Aluminium ladder product photo">
    <div class="panel panel-wide">
      <div class="card-brand">VORNEL LADDER</div>
      <p class="card-text">"VORNEL LADDER" ladders are made of both Aluminium and Fiberglass which are suitable for industry, business, shops, schools, home and garden. Find out VORNEL LADDER product range and choose the right tools for your application.<br>All VORNEL LADDER items are tested with EN131, AS/NZ and ANSI standards, you can easily find the best quality professional ladders in VORNEL LADDER's design. [...]</p>
      <a class="btn-outline">SHOP NOW</a>
    </div>
  </article>

  <article class="card c-logistic" role="img" aria-label="Roll container product photo">
    <div class="panel panel-narrow">
      <div class="card-brand">VORNEL LOGISTIC</div>
      <p class="card-text">VORNEL LOGISTIC provides all kinds of facilities to save your energy for transporting heavy goods Safely. Our items include roll containers, [...]</p>
      <a class="btn-outline">SHOP NOW</a>
    </div>
  </article>

  <article class="card c-castor" role="img" aria-label="Castor wheel and platform product photo">
    <div class="panel panel-narrow">
      <div class="card-brand">VORNEL CASTOR</div>
      <p class="card-text">Wheel and Castor. VORNEL CASTOR is to develop the best wheel, the best castor for all of our customer's requirements. Functionality, efficiency, [...]</p>
      <a class="btn-outline">SHOP NOW</a>
    </div>
  </article>

  <article class="card c-tools" role="img" aria-label="Safety tools and gloves product photo">
    <div class="panel panel-narrow">
      <div class="card-brand">VORNEL TOOLS</div>
      <p class="card-text">VORNEL TOOLS provides all kinds of Safety Equipments including insulated screwdrivers, multi-function gloves, shoes, helmet, harness, torch and more</p>
      <a class="btn-outline">SHOP NOW</a>
    </div>
  </article>

  <article class="card c-custom" role="img" aria-label="Technical drawing of a custom stair platform">
    <div class="panel panel-narrow">
      <div class="card-brand">VORNEL</div>
      <p class="card-text">Good design is important in working at height. Cannot find suitable item in the market ? Please write to us, we can make it for you exclusively.</p>
      <a class="btn-outline">CONTACT US</a>
    </div>
  </article>

  <article class="card c-scaffold" role="img" aria-label="Aluminium scaffold tower and parts product photo">
    <div class="panel panel-wide">
      <div class="card-brand" style="height:50px">VORNEL SCAFFOLD</div>
      <p class="card-text">Scaffolding requires Safety, Flexible combination, Easy assembling but strong at the same time. VORNEL SCAFFOLD ensures its maximum stability and Safe to use in all kinds of environments. The scaffold parts are made of high-quality aluminium profiles.</p>
      <a class="btn-outline">SHOP NOW</a>
    </div>
  </article>

  <footer class="site-footer">
    <svg class="footer-bg" width="767" height="150" viewBox="0 0 767 150" aria-hidden="true">
      <defs><linearGradient id="foot" x1="0" y1="0" x2="0" y2="1"><stop offset="0" stop-color="#d0d0d2"/><stop offset="1" stop-color="#bdbdc0"/></linearGradient></defs>
      <path d="M0,8 Q384,50 767,8 L767,150 L0,150 Z" fill="url(#foot)"/>
    </svg>
    <div class="brand-badge footer-badge"><span class="brand-name">VORNEL</span></div>
    <ul class="contact">
      <li><svg width="10" height="10" viewBox="0 0 24 24"><path fill="#d3202e" d="M6.6 10.8a15 15 0 0 0 6.6 6.6l2.2-2.2c.3-.3.7-.4 1-.2 1.1.4 2.3.6 3.6.6.6 0 1 .4 1 1V20c0 .6-.4 1-1 1A17 17 0 0 1 3 4c0-.6.4-1 1-1h3.5c.6 0 1 .4 1 1 0 1.3.2 2.5.6 3.6.1.3 0 .7-.2 1z"/></svg>+852 2975 1183</li>
      <li><svg width="11" height="9" viewBox="0 0 24 18"><rect width="24" height="18" rx="2" fill="#d3202e"/><path d="M1 2l11 8 11-8" stroke="#fff" stroke-width="2" fill="none"/></svg>info@vornel-climb.com</li>
      <li><svg width="9" height="12" viewBox="0 0 18 24"><path fill="#d3202e" d="M9 0a9 9 0 0 0-9 9c0 7 9 15 9 15s9-8 9-15a9 9 0 0 0-9-9z"/><circle cx="9" cy="9" r="3.5" fill="#fff"/></svg>Lorem ipsum dolor sit<br>amet, consectetue</li>
    </ul>
    <div class="social" aria-label="Social links"><span></span><span></span><span></span><span></span><span></span></div>
    <p class="copyright">©Copyright 2020 VORNEL All rights reserved.</p>
  </footer>

</div>
</body>
</html>
```